Business Card Design - Trelvo Services

Trelvo Services is a service company which carried out installation and maintenance work in the GPS Tracking industry.

We install and maintain GPS Tracking hardware into cars, trucks etc.

We have an existing design with existing logo which I would like to improve on. I would like to be able to edit the design in the future when we have new staff come on board. We currently have 8 or so different employees who would all require cards - ideally I need to be able to edit a template in photoshop or something.

The back of the existing design has a white outline of Australia with a white dot over: Brisbane, Sydney, Melbourne, Adelaide and Perth.

Our current cards are mainly black, our uniforms are black - happy to look at changing that if the look is right.

We strive to be organised, professional and we are working in the technology sector.

Cheers.

Industry/Entity Type

Business

Contact Information for Business Card

Name
Mobile number
Email address
Web address

Requirements
Must have
• Map of Australia as mentioned above.

```html
<!DOCTYPE html>
<html lang="en">
<head>
<meta charset="utf-8">
<title>Trelvo Services – Business Card</title>
<link rel="stylesheet" href="https://fonts.googleapis.com/css2?family=Questrial&display=swap">
<style>
  :root {
    --backdrop: #2a2a2a;
    --backdrop-edge: #141414;
    --card: #0b0b0b;
    --card-sheen: #171717;
    --ink: #ffffff;
    --ink-soft: #e4e4e4;
    --accent: #3d7fc4;
    --stripe-light: #f2f2f2;
    --stripe-shade: #bdbdbd;
    --map-tone: #1c1c1c;
  }
  * { box-sizing: border-box; margin: 0; padding: 0; }
  html, body { width: 1200px; height: 871px; overflow: hidden; }
  body {
    background: radial-gradient(ellipse at 50% 40%, var(--backdrop) 0%, var(--backdrop-edge) 100%);
    font-family: "Questrial", "Century Gothic", sans-serif;
    position: relative;
  }
  .card {
    position: absolute;
    top: 270px;
    width: 540px;
    height: 330px;
    background: linear-gradient(160deg, var(--card-sheen) 0%, var(--card) 55%);
    box-shadow: 0 18px 40px rgba(0,0,0,.6);
    overflow: hidden;
  }
  .card--back { left: 40px; }
  .card--front { left: 620px; }

  /* back */
  .australia-map {
    position: absolute;
    top: 22px;
    right: 40px;
    width: 250px;
    height: 200px;
    border-radius: 40% 45% 50% 40% / 45% 40% 55% 50%;
    background: radial-gradient(circle at 60% 40%, var(--map-tone), var(--card) 80%);
  }
  .card--back .wordmark {
    position: absolute;
    left: 36px;
    bottom: 40px;
    font-size: 34px;
    color: var(--accent);
  }

  /* front */
  .card--front .wordmark {
    position: absolute;
    top: 84px;
    right: 34px;
    font-size: 30px;
    color: var(--ink);
  }
  .holder {
    position: absolute;
    left: 62px;
    top: 136px;
  }
  .holder__name {
    font-size: 20px;
    letter-spacing: 2px;
    color: var(--ink);
    margin-bottom: 12px;
  }
  .contact-list { list-style: none; }
  .contact-list__item {
    display: flex;
    align-items: center;
    gap: 12px;
    height: 21px;
    font-size: 13.5px;
    letter-spacing: 1.2px;
    color: var(--ink-soft);
    margin-left: -28px;
  }
  .contact-list__icon { width: 16px; height: 16px; flex: none; }
  .contact-list__icon * { fill: none; stroke: var(--accent); stroke-width: 1.4; }
  .edge-stripe {
    position: absolute;
    left: 0;
    bottom: 0;
    width: 540px;
    height: 30px;
  }
</style>
</head>
<body>

  <section class="card card--back" aria-label="Card back">
    <div class="australia-map" role="img" aria-label="Outline map of Australia with dots marking Brisbane, Sydney, Melbourne, Adelaide and Perth"></div>
    <div class="wordmark">Trelvo Services</div>
  </section>

  <section class="card card--front" aria-label="Card front">
    <div class="wordmark">Trelvo Services</div>

    <div class="holder">
      <h1 class="holder__name">Dana Whitlock</h1>
      <ul class="contact-list">
        <li class="contact-list__item">
          <svg class="contact-list__icon" viewBox="0 0 16 16" aria-hidden="true"><path d="M3 2h3l1 3-2 1a8 8 0 0 0 5 5l1-2 3 1v3a1 1 0 0 1-1 1A12 12 0 0 1 2 3a1 1 0 0 1 1-1z"/></svg>
          <span>0400 555 018</span>
        </li>
        <li class="contact-list__item">
          <svg class="contact-list__icon" viewBox="0 0 16 16" aria-hidden="true"><rect x="4" y="1.5" width="8" height="4"/><rect x="1.5" y="5.5" width="13" height="6"/><rect x="4" y="9.5" width="8" height="5"/></svg>
          <span>(07) 5550 1234</span>
        </li>
        <li class="contact-list__item">
          <svg class="contact-list__icon" viewBox="0 0 16 16" aria-hidden="true"><rect x="1.5" y="3.5" width="13" height="9"/><path d="M1.5 3.5 8 9l6.5-5.5"/></svg>
          <span>dana@trelvoservices.com.au</span>
        </li>
        <li class="contact-list__item">
          <svg class="contact-list__icon" viewBox="0 0 16 16" aria-hidden="true"><circle cx="8" cy="8" r="6.5"/><ellipse cx="8" cy="8" rx="3" ry="6.5"/><path d="M1.5 8h13"/></svg>
          <span>www.trelvoservices.com.au</span>
        </li>
      </ul>
    </div>

    <svg class="edge-stripe" viewBox="0 0 540 30" preserveAspectRatio="none" aria-hidden="true">
      <defs>
        <linearGradient id="stripe-light-fill" x1="0" x2="1" y1="0" y2="0">
          <stop offset="0" stop-color="var(--stripe-light)"/>
          <stop offset="1" stop-color="var(--stripe-shade)"/>
        </linearGradient>
      </defs>
      <polygon points="0,2 330,2 310,30 0,30" fill="url(#stripe-light-fill)"/>
      <polygon points="338,12 540,12 540,30 326,30" fill="var(--accent)"/>
    </svg>
  </section>

</body>
</html>
```